Packaging design for aloe lotion bottle for a Laser Clinic

We need a packaging design for a body lotion bottle. Our business is a laser clinic and we are looking at slowly rolling out a range of skincare products. This lotion bottle is the first item with more to follow so the winning designer will have other designs to work on in the future.

The design needs to be classy, elegant, strong and sophisticated. The bottle will be clear with a shiny silver sleeved lid. The lotion itself, which will be visible through the bottle, will be a very light green colour. Think Mirelle Vantrau and Doriva as that is the image I want to convey.

Ideally we were thinking of having a design with a single colour but if you come up with a fantastic multi colour design that we love then we're open to it.

Reason: I have extended the deadline as I feel I need more time to allow designers to submit their designs. I haven't found a design that I love just yet. The project has been made a guaranteed payment upon completion. Thank you.

Target Market(s)

upper class high income earners with a high disposable income. People that look after themselves

Industry/Entity Type

Beauty Salon

Colors
000000
cadf82

Requirements
Must have
• must include the details below:
• After Beam Soothing Balm
• This soothing and calming anti inflammatory cream is specifically formulated for use after post laser treatments.
• Fresh Cucumber, Melon and Aloe Vera Leaf Juice blend together in perfect harmony to quickly cool you skin and restore your skins natural moisture.
• Our luxurious calming cream targets redness and helps to reduce inflammation, bringing you supple and radiant skin like never before.
• Directions: Use a liberal amount twice daily on all your treatment areas. This nourishing cream can also be used daily to restore moisture and softness to areas of the face and body not being treated by laser or IPL.
• Ingredients: water (aqua), glycine soja (soybean) oil, cetyl alcohol, glycerin dimethicone, butyrospermum parkii (shea butter), theobroma cacao (cocoa) seed butter, aloe barbadensis (aloe vera) leaf juice, tocopheryl acetate, sodium ascorbyl phosphate, disodium EDTA, ceteareth-20, carbomer, BHT, benzyl benzoate, butylphenyl methylpropional, hexyl cinnamal, linalool, glyceryl caprylate, methylisothiazolinone. May contain: Red 4 (CI 14700, aka 504), Yellow 5 (CI 19140, Ki4), Yellow 6 (CI 15985, KI5), Blue 1 (CI 42090, Ao1), Red 33 (CI 17200, Aka 227), Ext. Violet 2 (CI 60730, Murasaki401), Green 3 (CI 42053, Midori3)
• Against Animal Testing
• Manufactured in Australia
• www.velvetbloomclinic.example.com.au
• 500ml
• Pure Glow Laser Hair Removal logo (see attached files)
Nice to have
• A sophisticated and elegant design
Should not have
• no photos. not too many different colours

```html
<!DOCTYPE html>
<html lang="en">
<head>
<meta charset="utf-8">
<title>Pure Glow – After Beam Soothing Balm labels</title>
<link href="https://fonts.googleapis.com/css2?family=Raleway:wght@200;300;400;600;700;800&display=swap" rel="stylesheet">
<style>
  :root{
    --bg-top:#8a8a8a;
    --bg-bottom:#f4f4f4;
    --label:#1c1c1c;
    --label-light:#333333;
    --band:#141414;
    --ink:#e6e6e6;
    --ink-soft:#a8a8a8;
    --ink-dim:#8a8a8a;
    --lime:#9bc31c;
    --lime-soft:#cadf82;
  }
  *{box-sizing:border-box;margin:0;padding:0}
  html,body{width:1200px;height:1200px;overflow:hidden}
  body{
    background:linear-gradient(180deg,var(--bg-top) 0%,#c9c9c9 55%,var(--bg-bottom) 100%);
    font-family:"Raleway",sans-serif;
    color:var(--ink);
    position:relative;
  }
  .label{
    position:absolute;top:117px;width:400px;height:966px;
    background:radial-gradient(ellipse 120% 60% at 50% 55%,var(--label-light) 0%,var(--label) 55%,#0d0d0d 100%);
    border-radius:4px;overflow:hidden;
  }
  .label--front{left:170px}
  .label--back{left:630px}

  /* front */
  .brand-band{
    position:absolute;left:185px;top:0;width:153px;height:470px;background:var(--band);
    display:flex;justify-content:center;padding-top:46px;gap:6px;
  }
  .brand-band__name,.brand-band__tag{writing-mode:vertical-rl;white-space:nowrap}
  .brand-band__name{font-weight:700;font-size:62px;letter-spacing:-2px;color:var(--ink);line-height:1}
  .brand-band__tag{font-weight:400;font-size:21px;letter-spacing:7px;color:var(--ink);line-height:1;order:-1;margin-top:2px}

  .product-title{position:absolute;right:42px;top:548px;text-align:right}
  .product-title__main{font-size:40px;line-height:1;letter-spacing:-0.5px;color:var(--ink)}
  .product-title__main b{font-weight:800}
  .product-title__main span{font-weight:300}
  .product-title__sub{font-size:21px;font-weight:300;letter-spacing:5.5px;margin-top:4px}

  .front-intro{position:absolute;left:0;right:0;top:638px;text-align:center;font-size:13.5px;line-height:16px;font-weight:400;color:var(--ink)}
  .front-intro span{display:block;font-weight:300;color:var(--ink-soft)}
  .front-rule{position:absolute;left:36px;right:36px;top:714px;height:1px;background:var(--lime)}
  .ingredient-icons{position:absolute;left:0;right:0;top:737px;display:flex;justify-content:center;gap:5px}
  .ingredient-icons div{width:45px;height:45px;border-radius:50%;border:1.5px solid var(--lime);
    background:radial-gradient(circle,#5d7a0e 0%,#2a3508 70%,transparent 72%)}
  .front-blurb{position:absolute;left:0;right:0;top:803px;text-align:center;font-size:13.5px;line-height:15px;font-weight:400;color:var(--lime)}
  .volume{position:absolute;font-weight:300;font-size:17px;color:var(--ink-soft);letter-spacing:0.5px}
  .label--front .volume{left:0;right:0;top:915px;text-align:center}

  /* back */
  .back-brand{position:absolute;left:0;right:0;top:73px;text-align:center}
  .back-brand__name{font-size:34px;font-weight:700;letter-spacing:-1px;line-height:1}
  .back-brand__tag{font-size:11px;font-weight:600;letter-spacing:3.6px;margin-top:2px}
  .quote-rule{position:absolute;top:153px;left:33px;right:33px;height:30px}
  .quote-rule::before,.quote-rule::after{content:"";position:absolute;top:8px;width:132px;height:2px;background:var(--ink)}
  .quote-rule::before{left:0}.quote-rule::after{right:0}
  .quote-rule span{position:absolute;left:0;right:0;text-align:center;top:-6px;font-size:44px;font-weight:700;line-height:1}
  .back-pitch{position:absolute;left:24px;right:24px;top:184px;text-align:center;font-size:18.5px;font-weight:200;line-height:20.5px;color:var(--ink-soft)}
  .directions{position:absolute;left:24px;right:24px;top:300px;text-align:center;color:var(--ink-soft)}
  .directions h2{font-size:21px;font-weight:200;line-height:1}
  .directions p{font-size:13.5px;font-weight:200;line-height:17px}
  .ingredients{position:absolute;left:0;right:0;top:608px;height:137px;background:rgba(0,0,0,.35);padding:17px 18px 0;
    font-size:8px;line-height:13.8px;font-weight:300;color:var(--ink-dim);text-align:justify}
  .ingredients b{font-weight:700;color:var(--ink)}
  .support-rule{position:absolute;left:12px;right:16px;top:867px;height:2px;background:var(--ink)}
  .support{position:absolute;left:14px;top:880px}
  .support h3{font-size:11.5px;font-weight:400;color:var(--ink)}
  .support p{font-size:10px;font-weight:300;color:var(--ink-dim)}
  .support-row{position:absolute;left:14px;top:916px;display:flex;align-items:flex-end;gap:3px}
  .support-row .square{width:23px;height:23px;background:var(--ink)}
  .support-row small{font-size:7.5px;font-weight:300;color:var(--ink-dim);margin-left:7px}
  .badges{position:absolute;right:18px;top:884px;display:flex;align-items:center;gap:8px}
  .badge{width:48px;height:48px;border-radius:50%;border:1.5px solid var(--ink);background:transparent}
  .badge--small{width:30px;height:30px;background:var(--ink);border:none}
  .label--back .volume{right:18px;top:925px}
</style>
</head>
<body>
  <section class="label label--front" aria-label="Front label">
    <div class="brand-band">
      <div class="brand-band__name">PURE GLOW</div>
      <div class="brand-band__tag">LASER HAIR REMOVAL</div>
    </div>
    <div class="product-title">
      <div class="product-title__main"><b>AFTER</b> <span>BEAM</span></div>
      <div class="product-title__sub">SOOTHING BALM</div>
    </div>
    <p class="front-intro">This soothing and calming<br>anti inflammatory cream<span>is specifically formulated for use<br>after post laser treatments</span></p>
    <div class="front-rule"></div>
    <div class="ingredient-icons">
      <div role="img" aria-label="Cucumber slice icon"></div>
      <div role="img" aria-label="Melon slice icon"></div>
      <div role="img" aria-label="Aloe vera plant icon"></div>
    </div>
    <p class="front-blurb">Fresh Cucumber, Melon and Aloe Vera Leaf Juice<br>blend together in perfect harmony<br>to quickly cool you skin and<br>restore your skins natural moisture.</p>
    <div class="volume">500ml</div>
  </section>

  <section class="label label--back" aria-label="Back label">
    <div class="back-brand">
      <div class="back-brand__name">PURE GLOW</div>
      <div class="back-brand__tag">LASER HAIR REMOVAL</div>
    </div>
    <div class="quote-rule"><span>&ldquo;</span></div>
    <p class="back-pitch">Our luxurious calming cream targets redness and helps to reduce inflammation, bringing you supple and radiant skin like never before.</p>
    <div class="directions">
      <h2>Directions:</h2>
      <p>Use a liberal amount twice daily on all your treatment areas. This nourishing cream can also be used daily to restore moisture and softness to areas of the face and body not being treated by laser or IPL.</p>
    </div>
    <p class="ingredients"><b>Ingredients:</b> water (aqua), glycine soja (soybean) oil, cetyl alcohol, glycerin dimethicone, butyrospermum parkii (shea butter), theobroma cacao (cocoa) seed butter, aloe barbadensis (aloe vera) leaf juice, tocopheryl acetate, sodium ascorbyl phosphate, disodium EDTA, ceteareth-20, carbomer, BHT, benzyl benzoate, butylphenyl methylpropional, hexyl cinnamal, linalool, glyceryl caprylate, methylisothiazolinone. May contain: Red 4 (CI 14700, aka 504), Yellow 5 (CI 19140, Ki4), Yellow 6 (CI 15985, KI5), Blue 1 (CI 42090, Ao1), Red 33 (CI 17200, Aka 227), Ext. Violet 2 (CI 60730, Murasaki401), Green 3 (CI 42053, Midori3)</p>
    <div class="support-rule"></div>
    <div class="support">
      <h3>Customer Support</h3>
      <p>www.velvetbloomclinic.example.com.au</p>
    </div>
    <div class="support-row">
      <div class="square"></div><div class="square"></div>
      <small>Manufactured in Australia</small>
    </div>
    <div class="badges">
      <div class="badge" role="img" aria-label="Against animal testing badge"></div>
      <div class="badge badge--small" role="img" aria-label="Recyclable badge"></div>
    </div>
    <div class="volume">500ml</div>
  </section>
</body>
</html>
```